Professional business card for the wholesale of metals, chemicals and waste

We are an established company in the wholesale trade of metals, chemicals and waste and are looking for a creative, professional design for our business card. The business card should reflect the values of our company - competence, reliability and innovative strength. It should convey both industry expertise and a modern, trustworthy image.
Important information for the design:

Logo: Our company logo must be prominently placed on the business card.
Colors: Please refer to the colors used on our website www.okr-gmbh.at. These colors should appear in the design to maintain the visual identity of our company.

QR Code: The business card should contain a QR code that contains all the information listed on the business card.
Font: Choose clear, easy-to-read fonts that reflect a modern, professional look.
Layout: The design should be clear and structured so that both text and visual elements (logo, QR code) are in a balanced relationship to each other.

Information that should appear on the business card:

Company name: OKR Handelsagenturen GmbH
Title: Dipl.-Ing.
Name: Lukas Fenwald
Position: Managing Director of Operations & Corporate Development
Phone: +43 4186 5921 48
Mobile: +43 664 58 37 216
Email: lukas.fenwald@okr-gmbh.at
Homepage: www.okr-gmbh.at

Design style:

Industry: Industrial yet modern style that conveys competence and trust.
Message: The business card should present our company as a leading supplier in the wholesale trade of metals, chemicals and waste – reliable, professional and innovative.
Target group: Our target group consists of B2B customers and industry contacts who are looking for high-quality products and services in the areas of metal trading, chemicals and waste management.

We look forward to creative designs that reflect our professional identity and are also modern and appealing. Your design should make a statement for our company!

```html
<!DOCTYPE html>
<html lang="en">
<head>
<meta charset="utf-8">
<title>OKR Handelsagenturen GmbH – Business Card</title>
<link rel="stylesheet" href="https://fonts.googleapis.com/css2?family=Poppins:wght@400;700&display=swap">
<style>
  :root {
    --navy: #1f2249;
    --ink: #2a2a2e;
    --paper: #ffffff;
    --backdrop: #8a8a8c;
  }
  * { box-sizing: border-box; margin: 0; padding: 0; }
  html, body {
    width: 1093px;
    height: 1200px;
    overflow: hidden;
    background: var(--backdrop);
    font-family: "Poppins", sans-serif;
  }
  .card {
    position: absolute;
    left: 264px;
    width: 580px;
    height: 358px;
    border-radius: 27px;
    overflow: hidden;
  }
  .card--front { top: 226px; background: var(--paper); }
  .card--back  { top: 621px; background: var(--navy); }

  .accent-bar {
    position: absolute;
    left: 0; top: 35px;
    width: 16px; height: 54px;
    background: var(--navy);
  }
  .identity {
    position: absolute;
    left: 32px; top: 32px;
  }
  .identity__name {
    font-weight: 700;
    font-size: 19px;
    line-height: 22px;
    color: var(--navy);
    text-transform: uppercase;
    letter-spacing: -0.2px;
  }
  .identity__role {
    font-weight: 400;
    font-size: 17px;
    line-height: 21px;
    color: var(--ink);
  }
  .wordmark {
    position: absolute;
    font-weight: 700;
    line-height: 1;
    letter-spacing: 1px;
  }
  .card--front .wordmark {
    left: 289px; top: 90px;
    width: 244px; height: 157px;
    display: flex; align-items: center; justify-content: center;
    font-size: 86px;
    color: var(--navy);
  }
  .card--back .wordmark {
    inset: 0;
    display: flex; align-items: center; justify-content: center;
    font-size: 118px;
    color: var(--paper);
  }
  .contacts {
    position: absolute;
    left: 32px; top: 244px;
    list-style: none;
  }
  .contacts__item {
    display: flex;
    align-items: center;
    height: 21px;
    font-size: 17px;
    color: var(--ink);
  }
  .contacts__icon {
    width: 15px; height: 15px;
    margin-right: 7px;
    flex: none;
    fill: var(--navy);
  }
  .base-band {
    position: absolute;
    left: 0; bottom: 0;
    width: 100%; height: 17px;
    background: var(--navy);
  }
</style>
</head>
<body>
  <section class="card card--front" aria-label="Business card front">
    <div class="accent-bar"></div>
    <div class="identity">
      <h1 class="identity__name">Lukas Fenwald Dipl.-Ing.</h1>
      <p class="identity__role">Managing Director of Operations &amp;<br>Corporate Development</p>
    </div>
    <div class="wordmark">OKR</div>
    <ul class="contacts">
      <li class="contacts__item">
        <svg class="contacts__icon" viewBox="0 0 24 24" aria-hidden="true"><path d="M6.6 10.8a15.1 15.1 0 0 0 6.6 6.6l2.2-2.2a1 1 0 0 1 1-.25 11.4 11.4 0 0 0 3.6.57 1 1 0 0 1 1 1V20a1 1 0 0 1-1 1A17 17 0 0 1 3 4a1 1 0 0 1 1-1h3.5a1 1 0 0 1 1 1c0 1.25.2 2.45.57 3.57a1 1 0 0 1-.25 1z"/></svg>
        +43 4186 5921 48
      </li>
      <li class="contacts__item">
        <svg class="contacts__icon" viewBox="0 0 24 24" aria-hidden="true"><path d="M7 1h10a2 2 0 0 1 2 2v18a2 2 0 0 1-2 2H7a2 2 0 0 1-2-2V3a2 2 0 0 1 2-2zm0 3v14h10V4zm5 15.2a1.2 1.2 0 1 0 0 2.4 1.2 1.2 0 0 0 0-2.4z"/></svg>
        +43 664 58 37 216
      </li>
      <li class="contacts__item">
        <svg class="contacts__icon" viewBox="0 0 24 24" aria-hidden="true"><path d="M2 5h20v14H2zm2 2v.5l8 5.5 8-5.5V7l-8 5.5z"/></svg>
        lukas.fenwald@okr-gmbh.at
      </li>
      <li class="contacts__item">
        <svg class="contacts__icon" viewBox="0 0 24 24" aria-hidden="true"><path d="M12 2a10 10 0 1 0 0 20 10 10 0 0 0 0-20zm6.9 6h-2.9a15.6 15.6 0 0 0-1.4-3.6A8 8 0 0 1 18.9 8zM12 4a14 14 0 0 1 1.9 4h-3.8A14 14 0 0 1 12 4zM4.3 14a8 8 0 0 1 0-4h3.4a16.5 16.5 0 0 0 0 4zm.8 2h2.9a15.6 15.6 0 0 0 1.4 3.6A8 8 0 0 1 5.1 16zM8 8H5.1a8 8 0 0 1 4.3-3.6A15.6 15.6 0 0 0 8 8zm4 12a14 14 0 0 1-1.9-4h3.8A14 14 0 0 1 12 20zm2.3-6H9.7a14.7 14.7 0 0 1 0-4h4.6a14.7 14.7 0 0 1 0 4zm.3 5.6a15.6 15.6 0 0 0 1.4-3.6h2.9a8 8 0 0 1-4.3 3.6zm1.7-5.6a16.5 16.5 0 0 0 0-4h3.4a8 8 0 0 1 0 4z"/></svg>
        www.okr-gmbh.at
      </li>
    </ul>
    <div class="base-band"></div>
  </section>

  <section class="card card--back" aria-label="Business card back">
    <div class="wordmark">OKR</div>
  </section>
</body>
</html>
```